HML5 Web Application Design

We need a graphic design to give a HTML web application a modern look and feel. The design should be clean and neat with a metro inspired interface. All application uses vandrix controls so any experience with these would be great.
Perhaps you could also include a few screenshots of your previous work

Industry/Entity Type

Graphic Design

Requirements
Must have
• Must be HTML 5 compliant

```html
<!DOCTYPE html>
<html lang="en">
<head>
<meta charset="utf-8">
<title>Supplier Transactions</title>
<link href="https://fonts.googleapis.com/css2?family=Open+Sans:ital,wght@0,300;0,400;0,600;1,400&display=swap" rel="stylesheet">
<style>
  :root {
    --ink: #222222;
    --text: #333333;
    --muted: #555555;
    --soft: #888888;
    --accent: #ef4b3c;
    --link: #29a8e0;
    --rule: #d9d9d9;
    --header-bg: #ececec;
    --nav-active: #e8e8e8;
    --grid-accent: #5ab4e5;
    --footer-band: #c8c8c8;
    --pager-bg: #f5f5f5;
    --page: #ffffff;
  }
  * { box-sizing: border-box; margin: 0; padding: 0; }
  html, body { width: 1200px; height: 372px; overflow: hidden; background: var(--page); }
  body { position: relative; font-family: "Open Sans", sans-serif; color: var(--text); }

  .brand { position: absolute; left: 15px; top: 16px; display: flex; align-items: center; gap: 12px; }
  .brand-mark { width: 32px; height: 32px; background: var(--accent); border-radius: 50%; }
  .brand-name { font-size: 28px; font-weight: 400; color: var(--ink); letter-spacing: -0.3px; }

  .session { position: absolute; top: 14px; left: 984px; font-size: 12px; color: var(--text); white-space: nowrap; }
  .session .greeting { font-style: italic; }
  .session .user { color: var(--link); font-style: normal; margin-left: 4px; }
  .session .logoff { position: absolute; left: 115px; }

  .main-nav a { position: absolute; top: 75px; line-height: 32px; font-size: 14px; color: var(--text); text-decoration: none; white-space: nowrap; }
  .main-nav a.active { background: var(--nav-active); border-radius: 2px; width: 76px; text-align: center; }

  .page-title { position: absolute; left: 10px; top: 136px; font-size: 25px; font-weight: 300; color: var(--muted); white-space: nowrap; }

  .date-label { position: absolute; top: 145px; font-size: 12px; color: var(--text); white-space: nowrap; }
  .date-input { position: absolute; top: 136px; width: 165px; height: 32px; border: 1px solid var(--rule); background: var(--page); }
  .date-input svg { position: absolute; right: 7px; top: 9px; }

  .grid { position: absolute; left: 12px; top: 181px; width: 1134px; border-top: 2px solid var(--grid-accent); }
  .grid table { width: 100%; border-collapse: collapse; table-layout: fixed; }
  .grid th { background: var(--header-bg); height: 37px; text-align: left; font-weight: 400; font-size: 14px; color: var(--text); padding-left: 11px; position: relative; }
  .grid th .sort { position: absolute; top: 16px; }
  .grid td { height: 35px; padding-left: 11px; border-bottom: 1px solid var(--rule); font-size: 12.5px; color: var(--text); }
  .grid tbody tr:first-child td { height: 34px; }
  .col-date { width: 246px; } .col-type { width: 250px; } .col-ref { width: 258px; } .col-amount { width: 236px; }

  .pager { height: 34px; border: 1px solid var(--rule); border-top-color: #c4c4c4; background: var(--pager-bg); display: flex; align-items: center; justify-content: space-between; }
  .pager-controls { display: flex; height: 100%; }
  .pager-controls span { width: 23px; height: 100%; border-right: 1px solid var(--rule); display: flex; align-items: center; justify-content: center; color: var(--soft); font-size: 13px; }
  .pager-controls .page-num { color: var(--text); }
  .pager-info { font-size: 12.5px; color: var(--soft); padding-right: 11px; }

  .footer-band { position: absolute; left: 0; bottom: 0; width: 1200px; height: 20px; background: var(--footer-band); }
</style>
</head>
<body>
  <header>
    <div class="brand"><span class="brand-mark"></span><span class="brand-name">framewick</span></div>
    <div class="session"><span class="greeting">Hello,<span class="user">superuser!</span></span><span class="logoff">Log off</span></div>
    <nav class="main-nav">
      <a style="left:12px">Home</a>
      <a style="left:92px">Pin</a>
      <a style="left:152px">Request</a>
      <a style="left:245px">Transactions</a>
      <a style="left:366px">Tax</a>
      <a class="active" style="left:410px">Details</a>
      <a style="left:509px">Users</a>
      <a style="left:585px">Suppliers</a>
      <a style="left:685px">Queries</a>
      <a style="left:776px">LA Staff Queries</a>
    </nav>
  </header>

  <h1 class="page-title">Supplier Transactions Screen</h1>

  <span class="date-label" style="left:676px">Date From :</span>
  <span class="date-input" style="left:749px">
    <svg width="13" height="13" viewBox="0 0 13 13"><rect x="0.5" y="1.5" width="12" height="11" fill="none" stroke="#555"/><rect x="0.5" y="1.5" width="12" height="2.5" fill="#555"/><g fill="#555"><rect x="2" y="5.5" width="2" height="2"/><rect x="5.5" y="5.5" width="2" height="2"/><rect x="9" y="5.5" width="2" height="2"/><rect x="2" y="9" width="2" height="2"/><rect x="5.5" y="9" width="2" height="2"/><rect x="9" y="9" width="2" height="2"/></g></svg>
  </span>
  <span class="date-label" style="left:926px">Date To :</span>
  <span class="date-input" style="left:981px">
    <svg width="13" height="13" viewBox="0 0 13 13"><rect x="0.5" y="1.5" width="12" height="11" fill="none" stroke="#555"/><rect x="0.5" y="1.5" width="12" height="2.5" fill="#555"/><g fill="#555"><rect x="2" y="5.5" width="2" height="2"/><rect x="5.5" y="5.5" width="2" height="2"/><rect x="9" y="5.5" width="2" height="2"/><rect x="2" y="9" width="2" height="2"/><rect x="5.5" y="9" width="2" height="2"/><rect x="9" y="9" width="2" height="2"/></g></svg>
  </span>

  <section class="grid">
    <table>
      <thead>
        <tr>
          <th class="col-date">Date<svg class="sort" style="left:215px" width="9" height="5"><path d="M0 0h9L4.5 5z" fill="#999"/></svg></th>
          <th class="col-type">Type<svg class="sort" style="left:216px" width="9" height="5"><path d="M0 0h9L4.5 5z" fill="#999"/></svg></th>
          <th class="col-ref">Reference<svg class="sort" style="left:228px" width="9" height="5"><path d="M0 0h9L4.5 5z" fill="#999"/></svg></th>
          <th class="col-amount">Amount<svg class="sort" style="left:212px" width="9" height="5"><path d="M0 0h9L4.5 5z" fill="#999"/></svg></th>
          <th>Status<svg class="sort" style="left:115px" width="9" height="5"><path d="M0 0h9L4.5 5z" fill="#999"/></svg></th>
        </tr>
      </thead>
      <tbody>
        <tr><td>01/01/2013</td><td>Inv</td><td>12345</td><td>100</td><td>Received</td></tr>
        <tr><td>01/01/2013</td><td>Payment</td><td>456789</td><td>80</td><td>Payment</td></tr>
      </tbody>
    </table>
    <div class="pager">
      <div class="pager-controls">
        <span><svg width="9" height="9" viewBox="0 0 9 9"><path d="M1 1v7M7 1L3.5 4.5 7 8" fill="none" stroke="#888"/></svg></span>
        <span><svg width="9" height="9" viewBox="0 0 9 9"><path d="M6 1L2.5 4.5 6 8" fill="none" stroke="#888"/></svg></span>
        <span class="page-num">1</span>
        <span><svg width="9" height="9" viewBox="0 0 9 9"><path d="M3 1l3.5 3.5L3 8" fill="none" stroke="#888"/></svg></span>
        <span><svg width="9" height="9" viewBox="0 0 9 9"><path d="M2 1l3.5 3.5L2 8M8 1v7" fill="none" stroke="#888"/></svg></span>
      </div>
      <div class="pager-info">1 -2 of 2 items</div>
    </div>
  </section>

  <div class="footer-band"></div>
</body>
</html>
```